Construction company looking for modern

**Tallow Crest Joinery Limited**

We need a website for a renovation/remodeling company based in Hamilton, New Zealand. Ideally it will catch clients' attention and be modern and professional looking. I have attached a logo that I have just recently had made (through PixelHarbor). If the website could reflect this style and colour schemes, that would be awesome. The final design should communicate a trustworthiness and professionalism.

I have attached photos of a website that I really think is great, so if we could have something that follows along those likes,

https://www.dailyplover.example/local-news/news/local-builder-named-top-apprentice-for-region/QZTRPLA8VXN2MJ5DFYUEKHSWGO/

I won a competition a few years ago while I was an apprentice, If we could somehow put that in there as one of my achievements to try to bring in some trust that would be awesome. I would like to add a new picture though because my beard in that photo is wild.

Target Market(s)

Families that want live in the homes that i'm working on. not investors. People that are looking for quality not cheapest price.

Industry/Entity Type

Construction, Home renovations, Maintenance, Deck Builds, New Builds, Bathrooms, Kitchens

Coding

Coded - Design and coding required

Number of Pages Required

5+ page

Font styles to use
Sans Serif

Colors
6B429C
8869AF
B7A5CE
E3DAEB
F3F0F8

Requirements
Must have
• Contact us page, large clear pictures, Colours the work with the purple in my logo. That will be my company colour so I'm thinking black and purple, or what ever compliments purple nicely
Nice to have
• Page for Renovations, Testimonials, Contact us, Home, About us
Should not have
• Plain looking pages, empty white space, I want the text to be beside a nice big picture etc

```html
<!DOCTYPE html>
<html lang="en">
<head>
<meta charset="utf-8">
<title>Tallow Crest Joinery Ltd</title>
<link rel="stylesheet" href="https://fonts.googleapis.com/css2?family=Poppins:wght@400;500;600;700&display=swap">
<style>
:root{
  --purple:#6B429C;
  --purple-mid:#8869AF;
  --purple-soft:#B7A5CE;
  --purple-pale:#E3DAEB;
  --purple-mist:#F3F0F8;
  --ink:#1e1a24;
  --muted:#6d6873;
  --stone:#f4f2ef;
  --white:#ffffff;
  --star:#f2b833;
}
*{margin:0;padding:0;box-sizing:border-box}
html,body{width:1200px;height:5316px;overflow:hidden}
body{font-family:'Poppins',sans-serif;color:var(--ink);background:var(--white);position:relative}
.abs{position:absolute}
.label{position:absolute;left:0;width:1200px;text-align:center;color:var(--purple);font-size:15px;font-weight:600;letter-spacing:1.5px;text-transform:uppercase}
.heading{position:absolute;left:0;width:1200px;text-align:center;font-size:31px;font-weight:600;line-height:42px;color:var(--ink)}
.ph{position:absolute}

/* header */
.site-header{position:absolute;top:0;left:0;width:1200px;height:93px;background:var(--white);z-index:3}
.brand-disc{position:absolute;left:122px;top:-4px;width:146px;height:146px;border-radius:50%;background:var(--white);z-index:4;display:flex;align-items:center;justify-content:center;text-align:center}
.brand-name{font-size:15px;font-weight:700;color:var(--purple);line-height:18px;text-transform:uppercase}
.nav{position:absolute;top:38px;left:350px;display:flex;gap:0;font-size:13px;font-weight:500;letter-spacing:.5px}
.nav span{position:absolute;white-space:nowrap}
.call{position:absolute;left:902px;top:26px;display:flex;align-items:center;gap:14px}
.call-tri{width:40px;height:38px}
.call small{display:block;font-size:12px;color:var(--muted)}
.call b{font-size:16px;font-weight:700;letter-spacing:.5px}

/* hero */
.hero{position:absolute;top:93px;left:0;width:1200px;height:496px;background:linear-gradient(100deg,#3d2f45 0%,#6a5a5c 45%,#a89583 75%,#c8b8a4 100%)}
.hero-overlay{position:absolute;inset:0;background:linear-gradient(90deg,rgba(40,28,52,.75) 0%,rgba(40,28,52,.35) 55%,rgba(40,28,52,.1) 100%)}
.hero-kicker{position:absolute;left:122px;top:158px;color:var(--white);font-size:15px;letter-spacing:2.5px;font-weight:500}
.hero-title{position:absolute;left:122px;top:186px;color:var(--white);font-size:40px;font-weight:600;line-height:50px;width:520px}
.btn{position:absolute;display:flex;align-items:center;color:var(--white);font-size:14px;font-weight:600;letter-spacing:1.5px}
.btn .face{background:var(--purple);height:36px;display:flex;align-items:center;padding:0 28px;clip-path:polygon(0 0,100% 0,94% 100%,0 100%)}

/* about */
.about-text{position:absolute;left:626px;top:832px;width:440px;font-size:13.5px;line-height:21px;color:var(--muted)}
.name{position:absolute;left:281px;top:1300px;font-size:23px;font-weight:600}
.name-note{position:absolute;left:281px;top:1341px;font-size:11.5px;line-height:19px;color:var(--ink)}

/* services */
.svc-card{position:absolute;top:1643px;width:293px;height:355px}
.svc-card .cap{position:absolute;left:20px;bottom:22px;color:var(--white);font-size:17px;font-weight:600;letter-spacing:1.5px;line-height:24px}
.svc-card .go{position:absolute;right:24px;bottom:18px;width:46px;height:38px}

/* mission */
.mission{position:absolute;top:2277px;left:0;width:1200px;height:605px;background:var(--stone)}
.mission-copy{position:absolute;left:180px;top:2464px;width:840px;text-align:center;font-size:13.5px;line-height:25px;color:var(--muted)}
.pillar{position:absolute;top:2576px;width:213px;height:210px}
.pillar .txt{position:absolute;left:0;width:213px;top:132px;text-align:center;color:var(--white);font-size:14px;font-weight:600;line-height:20px}

/* testimonials */
.quote{position:absolute;top:3110px;width:340px}
.stars{color:var(--star);font-size:22px;letter-spacing:4px;line-height:22px}
.quote p{font-size:12.5px;line-height:21px;color:var(--muted);margin-top:10px}
.quote .who{margin-top:22px;font-size:13px;font-weight:600;color:var(--purple)}
.quote .where{font-size:11px;color:var(--muted);margin-left:22px}
.avatar{position:absolute;width:82px;height:82px;border-radius:50%}

/* gallery */
.shot{position:absolute;width:293px}
.shot .img{height:250px;position:relative}
.shot .tag{position:absolute;left:0;bottom:0;width:44px;height:44px}
.shot h3{font-size:19px;font-weight:600;letter-spacing:1px;line-height:24px;margin:12px 0 0 26px}

/* contact */
.contact{position:absolute;top:4314px;left:0;width:1200px;height:620px;background:linear-gradient(120deg,#3b3238 0%,#5b4f50 45%,#3e3439 100%)}
.contact-overlay{position:absolute;inset:0;background:rgba(30,22,32,.55)}
.form-card{position:absolute;left:171px;top:4488px;width:837px;height:301px;background:var(--white)}
.field{position:absolute;border:1px solid #e1dde4;font-size:13px;color:#555;padding:14px 0 0 12px}

/* footer */
.foot-head{position:absolute;font-size:14px;font-weight:600;letter-spacing:.5px}
.foot-head::before{content:"";display:inline-block;border-left:9px solid var(--purple);border-top:6px solid transparent;border-bottom:6px solid transparent;margin-right:14px;vertical-align:1px}
.foot-list{position:absolute;font-size:12.5px;color:var(--muted);line-height:29px}
.foot-rule{position:absolute;left:690px;top:5064px;width:1px;height:140px;background:#ddd}
.copyright{position:absolute;left:0;width:1200px;top:5282px;text-align:center;font-size:12px;color:var(--muted)}
</style>
</head>
<body>

<!-- Header -->
<header class="site-header">
  <nav class="nav">
    <span style="left:0">HOME</span>
    <span style="left:93px">ABOUT US</span>
    <span style="left:215px">SERVICES</span>
    <span style="left:312px">TESTIMONIALS</span>
    <span style="left:434px">CONTACT US</span>
  </nav>
  <div class="call">
    <svg class="call-tri" viewBox="0 0 40 38"><polygon points="20,0 40,38 0,38" fill="var(--purple)"/><path d="M15 20c2 4 4 6 8 8l2-2 3 2-2 3c-6-1-11-6-12-12l3-2 2 3z" fill="#fff"/></svg>
    <div><small>Call Us</small><b>(239) 555-0147</b></div>
  </div>
</header>
<div class="brand-disc"><span class="brand-name">Tallow Crest<br>Joinery<br>Ltd</span></div>

<!-- Hero -->
<section class="hero">
  <div class="ph" role="img" aria-label="Bright renovated open-plan living room and kitchen" style="inset:0"></div>
  <div class="hero-overlay"></div>
  <div class="hero-kicker">TALLOW CREST JOINERY LTD</div>
  <h1 class="hero-title">Your Trusted Partner in Home Renovations and Building Excellence</h1>
  <a class="btn" style="left:122px;top:378px"><span class="face">CONTACT US</span>
    <svg width="36" height="36" viewBox="0 0 36 36"><polygon points="2,36 20,2 34,36" fill="none" stroke="var(--purple-soft)" stroke-width="2"/><path d="M12 20h14m-5-5 5 5-5 5" stroke="#fff" stroke-width="2" fill="none"/></svg></a>
</section>

<!-- About -->
<div class="label" style="top:681px">About Us</div>
<h2 class="heading" style="top:712px">Bringing Your Vision to Life with Quality<br>Renovations and Construction</h2>
<svg class="abs" style="left:100px;top:864px" width="462" height="400" viewBox="0 0 462 400"><polygon points="0,400 178,0 450,0 450,8 186,8 18,400" fill="var(--purple)"/></svg>
<svg class="abs" style="left:100px;top:864px" width="182" height="400" viewBox="0 0 182 400"><polygon points="0,400 181,0 181,400" fill="var(--purple)"/></svg>
<div class="ph" role="img" aria-label="Smiling builder standing in a renovated living room" style="left:281px;top:872px;width:281px;height:392px;background:linear-gradient(160deg,#eef0ec,#c9cfc4 60%,#8fa08a)"></div>
<svg class="abs" style="left:130px;top:1256px" width="128" height="128" viewBox="0 0 128 128"><circle cx="64" cy="64" r="62" fill="#1d1b1a" stroke="#c9a64a" stroke-width="4"/><circle cx="64" cy="64" r="38" fill="#a98a3c"/></svg>
<div class="name">Marlo Kettering</div>
<div class="name-note">"Waikato's top building apprentice"<br>at the Regional Builders Apprentice Challenge</div>
<p class="about-text">At Tallow Crest Joinery LTD, we take pride in our ability to turn your dreams into reality. Our commitment to quality and dedication to craftsmanship are the cornerstones of our service. With years of experience, a winning spirit, and a passion for creating exceptional living spaces, we are your trusted partner in home renovations and construction.</p>
<div class="ph" role="img" aria-label="Modern lounge with fireplace and grey sofa" style="left:626px;top:1004px;width:432px;height:372px;background:linear-gradient(150deg,#e9e6e1,#b3aca5 55%,#5e5a57)"></div>
<svg class="abs" style="left:960px;top:1070px" width="210" height="306" viewBox="0 0 210 306"><polygon points="0,306 100,0 200,306" fill="none" stroke="rgba(255,255,255,.35)" stroke-width="20"/><polygon points="100,120 168,306 210,306 110,60" fill="var(--purple-mid)"/></svg>

<!-- Services -->
<div class="label" style="top:1536px">Services</div>
<h2 class="heading" style="top:1561px">Our Comprehensive Services</h2>
<div class="ph" role="img" aria-label="Bedroom with grey upholstered bed and ottoman" style="left:0;top:1632px;width:1200px;height:645px;background:linear-gradient(180deg,#f2f1ef 0%,#dedcd8 55%,#a7a49f 80%,#6f6b66 100%)"></div>
<div class="svc-card" style="left:140px">
  <div class="ph" role="img" aria-label="Renovated hallway" style="inset:0;background:linear-gradient(180deg,#d9d7d2,#8e8780 70%,#3e3935)"></div>
  <div class="cap">HOME<br>RENOVATIONS</div>
  <svg class="go" viewBox="0 0 46 38"><polygon points="0,0 46,0 46,38 14,38" fill="var(--purple)"/><path d="M16 19h18m-6-6 6 6-6 6" stroke="#fff" stroke-width="2.4" fill="none"/></svg>
</div>
<div class="svc-card" style="left:454px">
  <div class="ph" role="img" aria-label="Modern bathroom with stone walls" style="inset:0;background:linear-gradient(180deg,#cfccc6,#8a857e 70%,#3b3733)"></div>
  <div class="cap">BATHROOMS</div>
  <svg class="go" viewBox="0 0 46 38"><polygon points="0,0 46,0 46,38 14,38" fill="var(--purple)"/><path d="M16 19h18m-6-6 6 6-6 6" stroke="#fff" stroke-width="2.4" fill="none"/></svg>
</div>
<div class="svc-card" style="left:766px">
  <div class="ph" role="img" aria-label="White modern kitchen" style="inset:0;background:linear-gradient(180deg,#eceae6,#b2aea8 70%,#4b4742)"></div>
  <div class="cap">KITCHENS</div>
  <svg class="go" viewBox="0 0 46 38"><polygon points="0,0 46,0 46,38 14,38" fill="var(--purple)"/><path d="M16 19h18m-6-6 6 6-6 6" stroke="#fff" stroke-width="2.4" fill="none"/></svg>
</div>
<a class="btn" style="left:508px;top:2055px"><span class="face" style="height:34px">ALL SERVICES</span>
  <svg width="46" height="40" viewBox="0 0 46 40"><polygon points="2,38 24,2 44,38" fill="none" stroke="var(--purple)" stroke-width="2"/><path d="M14 24h18m-6-6 6 6-6 6" stroke="var(--purple)" stroke-width="2" fill="none"/></svg></a>

<!-- Mission -->
<section class="mission"></section>
<svg class="abs" style="left:526px;top:2204px" width="148" height="148" viewBox="0 0 148 148"><circle cx="74" cy="74" r="72" fill="#fff"/><circle cx="74" cy="74" r="60" fill="none" stroke="#1b1b1b" stroke-width="3"/><circle cx="74" cy="74" r="40" fill="#1b1b1b"/></svg>
<div class="label" style="top:2375px">Mission</div>
<h2 class="heading" style="top:2400px">Your Vision, Our Expertise</h2>
<p class="mission-copy">At Tallow Crest Joinery LTD, we understand that our target market consists of families seeking quality homes, not just investors looking for a quick profit. We know that your home is more than just a building; it's where you create cherished memories and lay the foundation for your family's future. That's why we offer:</p>

<div class="pillar" style="left:122px">
  <svg width="213" height="210" viewBox="0 0 213 210"><polygon points="106,10 213,210 0,210" fill="var(--purple)"/><circle cx="106" cy="56" r="56" fill="#fff" stroke="var(--purple)" stroke-width="3"/><path d="M84 70V54l18-14 18 14v16zM96 70V60h12v10" fill="none" stroke="var(--purple)" stroke-width="2.5"/><path d="M116 44l14-14" stroke="var(--purple)" stroke-width="3"/></svg>
  <div class="txt">CUSTOMIZED<br>SOLUTIONS</div>
</div>
<div class="pillar" style="left:356px">
  <svg width="213" height="210" viewBox="0 0 213 210"><polygon points="106,10 213,210 0,210" fill="var(--purple)"/><circle cx="106" cy="56" r="56" fill="#fff" stroke="var(--purple)" stroke-width="3"/><circle cx="106" cy="56" r="24" fill="none" stroke="var(--purple)" stroke-width="2.5"/><path d="M95 56l8 8 14-15" fill="none" stroke="var(--purple)" stroke-width="3"/></svg>
  <div class="txt">QUALITY<br>CRAFTSMANSHIP</div>
</div>
<div class="pillar" style="left:589px">
  <svg width="213" height="210" viewBox="0 0 213 210"><polygon points="106,10 213,210 0,210" fill="var(--purple)"/><circle cx="106" cy="56" r="56" fill="#fff" stroke="var(--purple)" stroke-width="3"/><rect x="84" y="38" width="44" height="34" fill="none" stroke="var(--purple)" stroke-width="2.5"/><path d="M94 72V56h24v16M90 46h32" fill="none" stroke="var(--purple)" stroke-width="2.5"/></svg>
  <div class="txt">ATTENTION TO<br>DETAIL</div>
</div>
<div class="pillar" style="left:822px">
  <svg width="213" height="210" viewBox="0 0 213 210"><polygon points="106,10 213,210 0,210" fill="var(--purple)"/><circle cx="106" cy="56" r="56" fill="#fff" stroke="var(--purple)" stroke-width="3"/><path d="M86 62v-8a20 20 0 0 1 40 0v8" fill="none" stroke="var(--purple)" stroke-width="2.5"/><rect x="82" y="58" width="8" height="14" fill="var(--purple)"/><rect x="122" y="58" width="8" height="14" fill="var(--purple)"/></svg>
  <div class="txt">EXPERT<br>CONSULTATION</div>
</div>

<!-- Testimonials -->
<div class="label" style="top:2991px">Testimonials</div>
<h2 class="heading" style="top:3016px">What our Customers Say</h2>
<div class="avatar" role="img" aria-label="Customer portrait" style="left:140px;top:3142px;background:linear-gradient(140deg,#e6d6c3,#a88f78)"></div>
<div class="quote" style="left:240px">
  <div class="stars">★★★★★</div>
  <p>"We couldn't be happier with the kitchen renovation Tallow Crest Joinery LTD completed for us. They took our vision and turned it into a reality, and the attention to detail was astounding."</p>
  <div class="who">— Priya and Tom K.</div>
  <div class="where">Hamilton, NZ</div>
</div>
<div class="avatar" role="img" aria-label="Customer portrait" style="left:620px;top:3142px;background:linear-gradient(140deg,#b9c3cc,#3f4a55)"></div>
<div class="quote" style="left:721px">
  <div class="stars">★★★★★</div>
  <p>"Tallow Crest Joinery LTD turned our house into a home. We entrusted them with a major renovation project, and the results were beyond our expectations."</p>
  <div class="who">— Priya and Tom K.</div>
  <div class="where">Hamilton, NZ</div>
</div>
<svg class="abs" style="left:560px;top:3340px" width="80" height="14" viewBox="0 0 80 14"><circle cx="4" cy="7" r="3" fill="#ccc"/><circle cx="22" cy="7" r="3" fill="#ccc"/><polygon points="40,1 46,12 34,12" fill="var(--purple)"/><circle cx="58" cy="7" r="3" fill="#ccc"/><circle cx="76" cy="7" r="3" fill="#ccc"/></svg>

<!-- Gallery -->
<div class="label" style="top:3416px">Gallery</div>
<h2 class="heading" style="top:3442px">Recent Projects</h2>
<div class="shot" style="left:140px;top:3523px"><div class="img" role="img" aria-label="Living room with sofa and round coffee table" style="background:linear-gradient(160deg,#efe9e0,#b7a48a 70%,#6d5a45)"><svg class="tag" viewBox="0 0 44 44"><polygon points="0,0 44,44 0,44" fill="var(--purple)"/><path d="M4 30h16m-5-5 5 5-5 5" stroke="#fff" stroke-width="2" fill="none"/></svg></div><h3>A Stunning Kitchen Renovation</h3></div>
<div class="shot" style="left:454px;top:3523px"><div class="img" role="img" aria-label="Neutral lounge with artwork and sofa" style="background:linear-gradient(160deg,#ebe6de,#b8ac9b 70%,#6a6054)"><svg class="tag" viewBox="0 0 44 44"><polygon points="0,0 44,44 0,44" fill="var(--purple)"/><path d="M4 30h16m-5-5 5 5-5 5" stroke="#fff" stroke-width="2" fill="none"/></svg></div><h3>A Stunning Kitchen Renovation</h3></div>
<div class="shot" style="left:766px;top:3523px"><div class="img" role="img" aria-label="White kitchen with island and large windows" style="background:linear-gradient(160deg,#f1f2f3,#bfc6cc 65%,#4e5760)"><svg class="tag" viewBox="0 0 44 44"><polygon points="0,0 44,44 0,44" fill="var(--purple)"/><path d="M4 30h16m-5-5 5 5-5 5" stroke="#fff" stroke-width="2" fill="none"/></svg></div><h3>A Stunning Kitchen Renovation</h3></div>
<div class="shot" style="left:140px;top:3878px"><div class="img" role="img" aria-label="Bedroom with orange bedding" style="background:linear-gradient(160deg,#d8d4cf,#8f8379 60%,#a8562d)"><svg class="tag" viewBox="0 0 44 44"><polygon points="0,0 44,44 0,44" fill="var(--purple)"/><path d="M4 30h16m-5-5 5 5-5 5" stroke="#fff" stroke-width="2" fill="none"/></svg></div><h3>A Stunning Kitchen Renovation</h3></div>
<div class="shot" style="left:454px;top:3878px"><div class="img" role="img" aria-label="Bright dining area with white chairs" style="background:linear-gradient(160deg,#f5f3ef,#d8d0c4 65%,#9c8f7e)"><svg class="tag" viewBox="0 0 44 44"><polygon points="0,0 44,44 0,44" fill="var(--purple)"/><path d="M4 30h16m-5-5 5 5-5 5" stroke="#fff" stroke-width="2" fill="none"/></svg></div><h3>A Stunning Kitchen Renovation</h3></div>
<div class="shot" style="left:766px;top:3878px"><div class="img" role="img" aria-label="Bedroom with dark headboard" style="background:linear-gradient(160deg,#8b8a8c,#4a4a50 60%,#d9d7d4)"><svg class="tag" viewBox="0 0 44 44"><polygon points="0,0 44,44 0,44" fill="var(--purple)"/><path d="M4 30h16m-5-5 5 5-5 5" stroke="#fff" stroke-width="2" fill="none"/></svg></div><h3>A Stunning Kitchen Renovation</h3></div>

<!-- Contact -->
<section class="contact">
  <div class="ph" role="img" aria-label="Staircase interior in dark tones" style="inset:0"></div>
  <div class="contact-overlay"></div>
</section>
<div class="label" style="top:4392px;color:#fff">Contact Us</div>
<h2 class="heading" style="top:4414px;color:#fff">Ready to Transform Your Space?</h2>
<div class="form-card"></div>
<div class="field" style="left:200px;top:4520px;width:390px;height:44px">Your name</div>
<div class="field" style="left:200px;top:4580px;width:390px;height:44px">Your phone</div>
<div class="field" style="left:200px;top:4640px;width:390px;height:44px">Your email</div>
<div class="field" style="left:606px;top:4520px;width:362px;height:164px">Message here</div>
<a class="btn" style="left:498px;top:4722px"><span class="face" style="height:38px">SUBMIT NOW</span>
  <svg width="48" height="42" viewBox="0 0 48 42"><polygon points="2,40 24,2 46,40" fill="none" stroke="var(--purple)" stroke-width="2"/><path d="M14 26h18m-6-6 6 6-6 6" stroke="var(--purple)" stroke-width="2" fill="none"/></svg></a>

<!-- Footer -->
<footer>
  <div class="abs" style="left:148px;top:5060px;width:170px;text-align:center"><span class="brand-name" style="font-size:18px;line-height:22px">Tallow Crest<br>Joinery Ltd</span></div>
  <svg class="abs" style="left:182px;top:5158px" width="92" height="30" viewBox="0 0 92 30"><circle cx="14" cy="15" r="14" fill="var(--purple)"/><circle cx="46" cy="15" r="14" fill="var(--purple)"/><circle cx="78" cy="15" r="14" fill="var(--purple)"/></svg>

  <div class="foot-head" style="left:399px;top:5000px">CONTACT INFORMATION</div>
  <svg class="abs" style="left:422px;top:5048px" width="14" height="100" viewBox="0 0 14 100"><path d="M7 1a6 6 0 0 0-6 6c0 5 6 11 6 11s6-6 6-11a6 6 0 0 0-6-6z" fill="var(--purple)"/><path d="M2 46c2 5 5 8 10 10l2-3-3-2-2 2c-2-1-3-2-4-4l2-2-2-3z" fill="var(--purple)"/><rect x="1" y="76" width="12" height="9" fill="var(--purple)"/></svg>
  <div class="foot-list" style="left:456px;top:5044px;line-height:17px;width:200px">418 Fernleigh Rd. Kestrel<br>Bay, Waikato 3204</div>
  <div class="foot-list" style="left:456px;top:5090px">+1 (555) 010-2299</div>
  <div class="foot-list" style="left:456px;top:5120px">info@tallowcrest.example</div>

  <div class="foot-head" style="left:690px;top:5000px">QUICK LINKS</div>
  <div class="foot-rule"></div>
  <div class="foot-list" style="left:712px;top:5040px">Home<br>About Us<br>Portfolio<br>Testimonials<br>Contact Us</div>

  <div class="foot-head" style="left:880px;top:5000px">SERVICES</div>
  <div class="foot-list" style="left:902px;top:5040px">Home Renovations<br>Maintenance<br>Deck Builds<br>Bathrooms<br>Kitchens<br>Customized Solutions</div>

  <div class="abs" style="left:0;top:5262px;width:1200px;height:1px;background:#e6e3e8"></div>
  <div class="copyright">© 2023 All Rights Reserved | Tallow Crest Joinery LTD</div>
</footer>

</body>
</html>
```